High-End audio shop owner needs a business card

I need a personal Business Card for my Audio shop which exists since 1962. We offer high Quality brands, professional Attention and run our own repair-service-department. I look for a design which will be printed on high Quality paper and shall convey trust to the Client that we are very serious. Language is german.

```html
<!DOCTYPE html>
<html lang="de">
<head>
<meta charset="utf-8">
<title>Klangwerk Auer – Visitenkarte</title>
<link href="https://fonts.googleapis.com/css2?family=Work+Sans:wght@400;500;700&display=swap" rel="stylesheet">
<style>
  :root {
    --backdrop: #3b3330;
    --card-grey: #7b7e7c;
    --card-grey-ink: #2a2b2b;
    --card-black: #1d1d1e;
    --accent: #f0661e;
    --text-light: #f2f2f2;
  }
  * { margin: 0; padding: 0; box-sizing: border-box; }
  html, body {
    width: 1200px; height: 716px; overflow: hidden;
    background: var(--backdrop);
    font-family: "Work Sans", Arial, sans-serif;
  }
  .canvas {
    width: 1200px; height: 716px;
    display: flex; align-items: center; justify-content: center; gap: 40px;
  }
  .card {
    width: 520px; height: 297px; border-radius: 4px;
    position: relative; overflow: hidden;
  }
  .card-front {
    background: var(--card-grey);
    display: flex; align-items: center; justify-content: center;
  }
  .front-name {
    color: var(--card-grey-ink);
    font-weight: 700; font-size: 30px; letter-spacing: 1px;
    text-transform: uppercase;
  }
  .card-back { background: var(--card-black); }
  .brand-name {
    position: absolute; left: 34px; top: 128px;
    color: var(--accent); font-weight: 700; font-size: 25px;
    text-transform: uppercase; letter-spacing: 0.5px;
  }
  .divider {
    position: absolute; left: 288px; top: 70px;
    width: 2px; height: 158px; background: var(--accent);
  }
  .contact {
    position: absolute; left: 312px; top: 66px;
    color: var(--text-light); font-size: 13.5px; line-height: 1.45;
  }
  .person-name {
    color: var(--accent); font-weight: 500; font-size: 19px;
    text-transform: uppercase; letter-spacing: 0.5px; line-height: 1.1;
  }
  .person-role { margin-bottom: 8px; }
  .address { margin-bottom: 4px; }
  .contact-line { display: flex; align-items: center; gap: 6px; }
  .contact-line svg { width: 10px; height: 10px; flex: none; }
</style>
</head>
<body>
<main class="canvas">
  <section class="card card-front">
    <span class="front-name">Klangwerk Auer</span>
  </section>

  <section class="card card-back">
    <span class="brand-name">Klangwerk Auer</span>
    <div class="divider"></div>
    <div class="contact">
      <p class="person-name">Jonas Berger</p>
      <p class="person-role">Director</p>
      <p class="address">27 Linden Row<br>Halden, ID 83100</p>
      <p class="contact-line">
        <svg viewBox="0 0 10 10"><path d="M2 0.5 L4 2.5 L3 3.8 Q4.2 6 6.2 7 L7.5 6 L9.5 8 L8 9.5 Q3 9 0.5 2 Z" fill="#f0661e"/></svg>
        555-014-2871
      </p>
      <p class="contact-line">
        <svg viewBox="0 0 10 10"><rect x="0.7" y="2" width="8.6" height="6" fill="none" stroke="#f0661e" stroke-width="1"/><path d="M0.7 2 L5 5.5 L9.3 2" fill="none" stroke="#f0661e" stroke-width="1"/></svg>
        info@klangwerkauer.com
      </p>
      <p class="contact-line">
        <svg viewBox="0 0 10 10"><circle cx="5" cy="5" r="4.3" fill="none" stroke="#f0661e" stroke-width="1"/><ellipse cx="5" cy="5" rx="1.8" ry="4.3" fill="none" stroke="#f0661e" stroke-width="0.8"/><path d="M0.7 5 H9.3" stroke="#f0661e" stroke-width="0.8"/></svg>
        www.klangwerkauer.com
      </p>
    </div>
  </section>
</main>
</body>
</html>
```